R&D and Engineering Management Consultancy Needs Branding

I need a branding style for my consultancy - specifically I need business cards by Tuesday 26 April (9 days away!) to take to a conference, including a logo design. If this service does not include printing I will need it in time for printing.

Later, the same logo and style needs to be incorporated into a Powerpoint template and a Word Template. Optionally also a Pages template.

The branding image needs to project and/or support the following qualities:
High tech
Speed and throughput
Lean
Innovation
Dependability
Quality

One possible concept is based on the Principal’s surname – Brannick, which is a small bird. So a logo design which is a stylized rendition of a bird may work well. Flight implies speed, and the style would be “techy”, perhaps geometric in a way that conveys Lean – boiling things down to the essential elements.

Other concepts are welcome.
You can find me on https://au.profilenetra.com/in/desmondbrannick

Business Card Information
Brannick Consulting
Desmond Brannick
BE (Hons), CSM, CSPO, SA
Principal Consultant
Mobile: +61 (0)455 903 617
Email: desmond@brannickconsulting.com
Web: www.brannickconsulting.com

Reverse:
Lean/Agile Software Development at Scale
Lean Product Development
Lean Portfolio Management
Organisational development and transformation
Mentoring and coaching of Technical Leaders
Program and project management
Business Processes and Systems

Target Market(s)

The target market for this consultancy comprises technology-based product and/or services development companies. They typically engage in one or a mix of software, electronics, mechanical, ASIC and MEMS development activities. They range from small startups to transnational corporations staffed by highly skilled engineers, developers and scientists. The consultancy is applicable across a range of domains such as biomedical device development, inkjet printing technology, telecommunications, internet and mesh networking technologies, renewable energy systems, and electronic product development of all kinds.

Industry/Entity Type

Information Technology

Contact Information for Business Card

Brannick Consulting
Desmond Brannick
BE (Hons), CSM, CSPO, SA
Principal Consulting

Reverse:
➢ Lean/Agile Software Development
➢ Lean Product Development
➢ Lean Portfolio Management
➢ Organisational development and transformation
➢ Mentoring and coaching of Technical Leaders
➢ Program and project management
➢ Business Processes and Systems

Logo Text

Just graphical

Font styles to use
Sans Serif

Requirements
Must have
• A clean professional look
Nice to have
• Use a bird motif based on my name Brannick
• The bird's colours are yellow/gold, light brown, black and red so these suggest a colour scheme.
• I have uploaded a stylised bird design that I like but this belongs to another company. A variation on this might be good.
Should not have
• Too much clutter. If the details are too much to fit, drop the qualifications line

```html
<!DOCTYPE html>
<html lang="en">
<head>
<meta charset="utf-8">
<title>Brannick Consulting – Business Card</title>
<link rel="stylesheet" href="https://fonts.googleapis.com/css2?family=Oxygen:wght@300;400;700&display=swap">
<style>
  :root {
    --canvas: #e9ebec;
    --paper: #ffffff;
    --ink: #2b2b2b;
    --black: #0d0d0d;
    --black-soft: #242424;
    --gold: #f5c400;
    --white: #ffffff;
  }
  * { box-sizing: border-box; margin: 0; padding: 0; }
  html, body { width: 1200px; height: 900px; overflow: hidden; }
  body {
    background: var(--canvas);
    font-family: "Oxygen", "Helvetica Neue", Arial, sans-serif;
    display: flex;
    flex-direction: column;
    align-items: center;
    justify-content: center;
    gap: 48px;
  }
  .card {
    position: relative;
    width: 620px;
    height: 376px;
    background: var(--paper);
    box-shadow: 0 6px 18px rgba(0,0,0,0.12);
    overflow: hidden;
  }
  .card-art { position: absolute; inset: 0; }

  /* Company name set in plain text as brand placeholder */
  .brand-name {
    position: absolute;
    color: var(--ink);
    font-weight: 400;
    white-space: nowrap;
    line-height: 1.1;
  }

  /* Front */
  .front .brand-name { left: 32px; top: 200px; font-size: 20px; }
  .holder { position: absolute; left: 330px; top: 118px; }
  .holder-name { color: var(--gold); font-size: 25px; font-weight: 700; }
  .holder-role { color: var(--white); font-size: 16px; font-weight: 300; margin-top: 2px; }
  .contacts { position: absolute; left: 330px; top: 222px; list-style: none; }
  .contacts li {
    display: flex; align-items: center; gap: 10px;
    color: var(--white); font-size: 14px; font-weight: 300;
    height: 24px;
  }
  .contacts svg { width: 13px; height: 13px; flex: none; }

  /* Back */
  .back .brand-name { left: 52px; top: 58px; font-size: 26px; }
  .services { position: absolute; left: 52px; top: 124px; list-style: none; }
  .services li {
    display: flex; align-items: center; gap: 9px;
    color: var(--ink); font-size: 15px; font-weight: 400;
    height: 24px;
  }
  .services svg { width: 12px; height: 10px; flex: none; }
  .web-line { font-family: "Oxygen", Arial, sans-serif; font-size: 17px; fill: var(--white); }
</style>
</head>
<body>

  <!-- Front of card -->
  <section class="card front" aria-label="Business card front">
    <svg class="card-art" viewBox="0 0 620 376" aria-hidden="true">
      <defs>
        <linearGradient id="panel-front" x1="0" y1="0" x2="1" y2="1">
          <stop offset="0" stop-color="var(--black)"/>
          <stop offset="1" stop-color="var(--black-soft)"/>
        </linearGradient>
      </defs>
      <path d="M270 0 Q196 210 356 376" fill="none" stroke="var(--gold)" stroke-width="5"/>
      <path d="M276 0 Q204 210 364 376 L620 376 L620 0 Z" fill="url(#panel-front)"/>
    </svg>

    <div class="brand-name">Brannick Consulting</div>

    <div class="holder">
      <div class="holder-name">Desmond Brannick</div>
      <div class="holder-role">Principal Consulting</div>
    </div>

    <ul class="contacts">
      <li>
        <svg viewBox="0 0 14 14"><rect x="3" y="0.5" width="8" height="13" rx="1.5" fill="var(--gold)"/><rect x="4.5" y="2.5" width="5" height="7" fill="var(--black)"/></svg>
        +61 (0)455 903 617
      </li>
      <li>
        <svg viewBox="0 0 14 14"><rect x="0.5" y="3" width="13" height="9" fill="var(--gold)"/><path d="M0.5 3 L7 8 L13.5 3" fill="none" stroke="var(--black)" stroke-width="1.2"/></svg>
        desmond@brannickconsulting.com
      </li>
      <li>
        <svg viewBox="0 0 14 14"><circle cx="7" cy="7" r="6.5" fill="var(--gold)"/><g fill="none" stroke="var(--black)" stroke-width="0.9"><ellipse cx="7" cy="7" rx="2.6" ry="6"/><path d="M1 7 H13 M2 4 H12 M2 10 H12"/></g></svg>
        www.brannickconsulting.com
      </li>
    </ul>
  </section>

  <!-- Back of card -->
  <section class="card back" aria-label="Business card back">
    <svg class="card-art" viewBox="0 0 620 376" aria-hidden="true">
      <defs>
        <linearGradient id="panel-back" x1="0" y1="1" x2="1" y2="0">
          <stop offset="0" stop-color="var(--black)"/>
          <stop offset="1" stop-color="var(--black-soft)"/>
        </linearGradient>
        <path id="web-curve" d="M372 362 Q520 300 612 178"/>
      </defs>
      <path d="M226 376 Q470 330 620 122" fill="none" stroke="var(--gold)" stroke-width="5"/>
      <path d="M236 376 Q476 336 620 132 L620 376 Z" fill="url(#panel-back)"/>
      <g transform="translate(356 360) rotate(-22)">
        <circle r="8" fill="var(--gold)"/>
        <g fill="none" stroke="var(--black)" stroke-width="1">
          <ellipse rx="3.2" ry="7.3"/>
          <path d="M-7.5 0 H7.5 M-6.5 -3.6 H6.5 M-6.5 3.6 H6.5"/>
        </g>
      </g>
      <text class="web-line"><textPath href="#web-curve">www.brannickconsulting.com</textPath></text>
    </svg>

    <div class="brand-name">Brannick Consulting</div>

    <ul class="services">
      <li><svg viewBox="0 0 12 10"><path d="M0 0 L12 5 L0 10 L3 5 Z" fill="var(--gold)"/></svg>Lean/Agile Software Development at Scale</li>
      <li><svg viewBox="0 0 12 10"><path d="M0 0 L12 5 L0 10 L3 5 Z" fill="var(--gold)"/></svg>Lean Product Development</li>
      <li><svg viewBox="0 0 12 10"><path d="M0 0 L12 5 L0 10 L3 5 Z" fill="var(--gold)"/></svg>Lean Portfolio Management</li>
      <li><svg viewBox="0 0 12 10"><path d="M0 0 L12 5 L0 10 L3 5 Z" fill="var(--gold)"/></svg>Organisational development and transformation</li>
      <li><svg viewBox="0 0 12 10"><path d="M0 0 L12 5 L0 10 L3 5 Z" fill="var(--gold)"/></svg>Mentoring and coaching of Technical Leaders</li>
      <li><svg viewBox="0 0 12 10"><path d="M0 0 L12 5 L0 10 L3 5 Z" fill="var(--gold)"/></svg>Program and project management</li>
      <li><svg viewBox="0 0 12 10"><path d="M0 0 L12 5 L0 10 L3 5 Z" fill="var(--gold)"/></svg>Business Processes and Systems</li>
    </ul>
  </section>

</body>
</html>
```